High profile consulting company needs a Business Card Design

I need a business card design for a coaching /consulting company. We specialize in changing behaviors. Our services include therapy, workshops, life coaching, etc.

Check out our website to get a feel for our personality. www.tidewaterguidance.com

The new logo will be attached to the website soon, I have attached the new logo for your use on the business card.
Updates

I forgot to provide you with the company email under the "must have" section for the business card.  The website is:

 www.tidewaterguidance.com

I understand there's some trouble with the logo I uploaded.  I will try that again.  Thank you for your efforts.

Lauren

Thank you for some of your questions.  I prefer a one sided business card, and tend to like the white backgrounds.

I also made 2 small changes to the content.  

add MFT after the name:  Lauren Pettigrew, MFT

and the tag line needed more clarity once I saw it.  Please change it to:  Improving performance by strengthening relationships and changing behaviors.

Thank you,
Lauren

Industry/Entity Type

Business

Requirements
Must have
• logo
Phone number: 321-555-0164
email: Lauren@tidewaterguidance.com
Lauren Pettigrew, MFT
President
Nice to have
• Improving performance by strengthening relationships and changing behaviors.

```html
<!DOCTYPE html>
<html lang="en">
<head>
<meta charset="utf-8">
<title>Tidewater Guidance — Business Card</title>
<link rel="stylesheet" href="https://fonts.googleapis.com/css2?family=Open+Sans:wght@400;700;800&display=swap">
<style>
  :root {
    --stage: #141414;
    --card-dark: #1a1a1a;
    --card-mid: #383838;
    --band: #ffffff;
    --ink: #151515;
    --accent: #0f7a55;
    --mark-fill: #5e5e5e;
    --text-light: #f2f2f2;
    --text-muted: #c9c9c9;
  }
  * { margin: 0; padding: 0; box-sizing: border-box; }
  html, body {
    width: 1200px;
    height: 900px;
    overflow: hidden;
    background: var(--stage);
    font-family: "Open Sans", Arial, sans-serif;
  }
  .card {
    position: absolute;
    left: 250px;
    width: 700px;
    height: 400px;
    overflow: hidden;
    border-radius: 4px;
    background: radial-gradient(ellipse at 40% 45%, var(--card-mid) 0%, var(--card-dark) 80%);
    box-shadow: 0 14px 36px rgba(0,0,0,0.6);
  }
  .card-back { top: 35px; }
  .card-front { top: 465px; }

  /* back side */
  .back-ring {
    position: absolute;
    left: -70px;
    top: 40px;
    width: 330px;
    height: 330px;
    border-radius: 50%;
    background: rgba(255,255,255,0.06);
    border: 10px solid rgba(15,122,85,0.35);
  }
  .back-brand {
    position: absolute;
    left: 300px;
    top: 70px;
    width: 280px;
    text-align: center;
  }
  .back-dot {
    width: 110px;
    height: 110px;
    margin: 0 auto 14px;
    border-radius: 50%;
    background: var(--mark-fill);
    border: 6px solid var(--accent);
  }
  .back-name {
    font-weight: 700;
    font-size: 22px;
    letter-spacing: 1px;
    color: var(--text-light);
    text-transform: uppercase;
    white-space: nowrap;
  }

  /* front side */
  .brand-band {
    position: absolute;
    left: 0;
    top: 88px;
    width: 100%;
    height: 80px;
    background: var(--band);
  }
  .brand-dot {
    position: absolute;
    left: 26px;
    top: 66px;
    width: 104px;
    height: 104px;
    border-radius: 50%;
    background: var(--mark-fill);
    border: 6px solid var(--accent);
  }
  .brand-name {
    position: absolute;
    left: 150px;
    top: 104px;
    font-weight: 800;
    font-size: 38px;
    line-height: 48px;
    color: var(--ink);
    text-transform: uppercase;
    white-space: nowrap;
  }
  .contact {
    position: absolute;
    left: 38px;
    top: 205px;
    color: var(--text-muted);
    font-family: Arial, "Open Sans", sans-serif;
    font-size: 13px;
    line-height: 1.35;
  }
  .contact-label {
    color: var(--text-light);
    font-weight: 700;
    text-transform: uppercase;
  }
  .contact-group + .contact-group { margin-top: 12px; }
  .person {
    position: absolute;
    right: 38px;
    top: 190px;
    text-align: right;
    color: var(--text-light);
  }
  .person-name {
    font-size: 28px;
    font-weight: 400;
    line-height: 1.15;
  }
  .person-title {
    font-size: 16px;
    font-weight: 400;
    line-height: 1.2;
  }
</style>
</head>
<body>
  <section class="card card-back">
    <div class="back-ring"></div>
    <div class="back-brand">
      <div class="back-dot"></div>
      <div class="back-name">Tidewater Guidance</div>
    </div>
  </section>

  <main class="card card-front">
    <div class="brand-band"></div>
    <div class="brand-dot"></div>
    <div class="brand-name">Tidewater Guidance</div>

    <section class="contact">
      <div class="contact-group">
        <div class="contact-label">Web</div>
        <div>www.tidewaterguidance.com</div>
        <div>Lauren@tidewaterguidance.com</div>
      </div>
      <div class="contact-group">
        <div class="contact-label">Telephone</div>
        <div>: 321-555-0164</div>
      </div>
    </section>

    <section class="person">
      <div class="person-name">Lauren Pettigrew</div>
      <div class="person-title">MFT, President</div>
    </section>
  </main>
</body>
</html>
```